Tamarack Hearth Partners Business Card

Looking for a new business card layout. We are a real estate firm w/ a logo, old design attached. Must keep the same elements on there, just need a fresh look and possible some foil accents. Looking for a simpler design w/ more modern style.

Target Market(s)

Real Estate clients

Industry/Entity Type

Real Estate Agent

Contact Information for Business Card

see attached

Font styles to use
Sans Serif

Requirements
Must have
• all elements on current biz card
Nice to have
• modern look, simpler than we have!
Should not have
• no serif fonts

```html
<!DOCTYPE html>
<html lang="en">
<head>
<meta charset="utf-8">
<title>Tamarack Hearth Partners – Business Card</title>
<link href="https://fonts.googleapis.com/css2?family=Montserrat:wght@300;400;700;800&display=swap" rel="stylesheet">
<style>
  :root {
    --stage: #d4d5d4;
    --card: #0d0d0d;
    --gold: #c3912f;
    --gold-soft: #d9b57a;
    --white: #ffffff;
    --muted: #e6e6e6;
    --photo-top: #d8cfc4;
    --photo-bottom: #3fb9b4;
  }
  * { box-sizing: border-box; margin: 0; padding: 0; }
  html, body { width: 1200px; height: 900px; overflow: hidden; }
  body {
    background: var(--stage);
    font-family: "Montserrat", sans-serif;
    display: flex;
    align-items: center;
    justify-content: center;
    gap: 80px;
  }
  .card {
    width: 400px;
    height: 700px;
    background: var(--card);
    position: relative;
    box-shadow: 0 10px 24px rgba(0,0,0,0.25);
    overflow: hidden;
  }
  .brand-name {
    color: var(--gold);
    font-weight: 800;
    text-transform: uppercase;
    text-align: center;
    line-height: 1.05;
  }
  .card-back {
    display: flex;
    align-items: center;
    justify-content: center;
  }
  .card-back .brand-name { font-size: 44px; letter-spacing: 1px; }

  .card-front { display: flex; flex-direction: column; align-items: center; }
  .card-front .brand-name { font-size: 24px; margin-top: 40px; letter-spacing: 0.5px; }
  .agent-photo {
    width: 250px;
    height: 290px;
    margin-top: 26px;
    background: linear-gradient(180deg, var(--photo-top) 0%, #efe2cf 55%, var(--photo-bottom) 100%);
  }
  .agent-name {
    color: var(--gold);
    font-weight: 800;
    font-size: 30px;
    text-transform: uppercase;
    margin-top: 18px;
    letter-spacing: 0.5px;
  }
  .agent-title { color: var(--muted); font-weight: 300; font-size: 16px; margin-top: 2px; }
  .contact {
    align-self: stretch;
    padding: 22px 40px 0;
    color: var(--white);
  }
  .address { font-weight: 300; font-size: 15px; margin-bottom: 10px; }
  .phone {
    display: flex;
    align-items: center;
    gap: 10px;
    font-weight: 700;
    font-size: 27px;
    letter-spacing: 0.5px;
    line-height: 1.2;
  }
  .phone svg { width: 20px; height: 22px; flex: none; }
  .email { font-weight: 300; font-size: 17px; margin-top: 6px; }
  .web-band {
    position: absolute;
    left: 0; right: 0; bottom: 0;
    height: 56px;
    background: var(--gold);
    color: var(--white);
    display: flex;
    align-items: center;
    justify-content: center;
    font-size: 17px;
    font-weight: 400;
  }
  .web-band strong { font-weight: 700; }
</style>
</head>
<body>
  <section class="card card-back">
    <p class="brand-name">Tamarack<br>Hearth<br>Partners</p>
  </section>

  <section class="card card-front">
    <p class="brand-name">Tamarack Hearth<br>Partners</p>
    <div class="agent-photo" role="img" aria-label="Portrait photo of the agent"></div>
    <p class="agent-name">Dana Whitlock</p>
    <p class="agent-title">Principal Broker</p>
    <div class="contact">
      <p class="address">482 Alder Ridge Rd, Sisters, OR 97759</p>
      <p class="phone">
        <svg viewBox="0 0 20 22" aria-hidden="true"><path d="M4 1 L8 1 L9 6 L6.5 8 C8 11.5 10.5 14 14 15.5 L16 13 L19 14 L19 19 C19 20 18 21 17 21 C8 20 1 13 1 4 C1 2 2 1 4 1 Z" fill="var(--gold)"/></svg>
        555.204.7180
      </p>
      <p class="phone">
        <svg viewBox="0 0 20 22" aria-hidden="true"><rect x="4" y="1" width="12" height="20" rx="2" fill="none" stroke="var(--gold)" stroke-width="1.8"/><line x1="8" y1="17.5" x2="12" y2="17.5" stroke="var(--gold)" stroke-width="1.6"/></svg>
        555.318.6042
      </p>
      <p class="email">dana@tamarackhearth.com</p>
    </div>
    <div class="web-band">www.<strong>TamarackHearth-Homes</strong>.com</div>
  </section>
</body>
</html>
```